Lifestyle brand needs lip balm label design

We need a label design for lip balm tubes. The name of our company is "lorvanquill"

Design Description:
Our lip balm tubes will be black. The label itself will be clear/transparent. We would like to create a gradient effect with the color green (same shade as our logo) starting from the bottom and slowly fading out to clear so that the black tube is visible (example of gradient shown in attached image)

We have two lip balm flavors: mint and lemongrass.
We would like the top/clear portion of the label to say "MINT" (all caps) . The second label should say "LEMONGRASS" (all caps) in the same location. Our logo "lorvanquill" should be in the bottom/green portion of the label. Below the logo, we would like the words "NATURAL BALM" (all caps) in white text

```html
<!DOCTYPE html>
<html lang="en">
<head>
<meta charset="utf-8">
<title>lorvanquill — Mint Natural Balm Label</title>
<link rel="stylesheet" href="https://fonts.googleapis.com/css2?family=Jost:wght@400;500&family=Aldrich&display=swap">
<style>
  :root {
    --page: #ffffff;
    --tube-black: #000000;
    --fade-mid: #3a3f2e;
    --leaf-green: #5b7a37;
    --base-green: #528526;
    --lime: #e0f08a;
    --ink: #000000;
    --mark-glow: #eef2c8;
  }
  * { margin: 0; padding: 0; box-sizing: border-box; }
  html, body {
    width: 1200px;
    height: 918px;
    overflow: hidden;
    background: var(--page);
  }
  .canvas {
    position: relative;
    width: 1200px;
    height: 918px;
  }
  .label {
    position: absolute;
    left: 409px;
    top: 200px;
    width: 382px;
    height: 518px;
    background: linear-gradient(
      to bottom,
      var(--tube-black) 0%,
      var(--tube-black) 35%,
      var(--fade-mid) 47%,
      var(--leaf-green) 58%,
      var(--base-green) 100%
    );
    overflow: hidden;
  }
  .flavour {
    position: absolute;
    top: 52px;
    left: 0;
    width: 100%;
    text-align: center;
    font-family: "Jost", sans-serif;
    font-weight: 500;
    font-size: 54px;
    line-height: 1;
    letter-spacing: -1px;
    color: var(--lime);
    transform: scaleX(0.86);
  }
  .flavour-illustration {
    position: absolute;
    left: 50px;
    top: 85px;
    width: 233px;
    height: 208px;
    border-radius: 50% 40% 45% 55%;
    background: radial-gradient(
      ellipse at 60% 65%,
      rgba(224, 240, 138, 0.55) 0%,
      rgba(238, 242, 200, 0.18) 45%,
      rgba(238, 242, 200, 0) 72%
    );
  }
  .brand-band {
    position: absolute;
    top: 338px;
    left: 0;
    width: 100%;
    height: 55px;
    background: var(--lime);
    display: flex;
    align-items: center;
    justify-content: center;
  }
  .brand-name {
    font-family: "Jost", sans-serif;
    font-weight: 400;
    font-size: 40px;
    line-height: 1;
    color: var(--ink);
    letter-spacing: 0.5px;
    padding-bottom: 6px;
  }
  .product-line {
    position: absolute;
    top: 428px;
    left: 10px;
    right: 17px;
    display: flex;
    align-items: center;
    gap: 10px;
  }
  .product-line .rule {
    flex: 1;
    height: 1px;
    background: var(--lime);
  }
  .product-name {
    font-family: "Aldrich", sans-serif;
    font-size: 26px;
    line-height: 1;
    color: var(--ink);
    white-space: nowrap;
    transform: scaleX(0.88);
    margin: 0 -10px;
  }
  .volume {
    position: absolute;
    top: 483px;
    left: 0;
    width: 100%;
    text-align: center;
    font-family: "Aldrich", sans-serif;
    font-size: 7px;
    letter-spacing: 0.5px;
    color: var(--ink);
  }
</style>
</head>
<body>
  <main class="canvas">
    <section class="label">
      <h1 class="flavour">MINT</h1>
      <div class="flavour-illustration" role="img" aria-label="Flowing swoosh lines and a mint leaf illustration"></div>
      <div class="brand-band">
        <span class="brand-name">lorvanquill</span>
      </div>
      <div class="product-line">
        <span class="rule"></span>
        <span class="product-name">NATURAL BALM</span>
        <span class="rule"></span>
      </div>
      <p class="volume">100ml</p>
    </section>
  </main>
</body>
</html>
```